TRENDY & MODERN BUSINESS CARD DESIGN for Media Company *

I need a minimalistic - clean - modern and professional business card layout and design for MEDIA & PHOTOGRAPHY STUDIO.

We do NOT have a logo, and not really looking for one - but rather excellent typography and design. We would consider the 3 as a focal point.

We do personal and commercial photography.

Target Market(s)

Personal and commercial photography clientele

Contact Information for Business Card

ZUB size - from zub.com / size guidelines are enclosed in the brief

Font styles to use
Sans Serif

Colors
f78f20
eda3c7
cee9f5
0555a3
e667a6
fbf289

Requirements
Must have
• Clean lines - Modern layout
Nice to have
• All blue background as an option - use color palette in brief please.
Should not have
• Old fashion fonts and regular fonts.

```html
<!DOCTYPE html>
<html lang="en">
<head>
<meta charset="utf-8">
<title>Brightwell Media — Business Card</title>
<link href="https://fonts.googleapis.com/css2?family=Open+Sans:wght@400;600&display=swap" rel="stylesheet">
<style>
  :root {
    --brand-blue: #0b4f96;
    --paper: #ffffff;
    --ink: #1d1d1f;
    --backdrop: #e9ecef;
    --card-shadow: rgba(20, 30, 50, 0.18);
  }
  * { box-sizing: border-box; margin: 0; padding: 0; }
  html, body {
    width: 1200px; height: 1200px; overflow: hidden;
    background: var(--backdrop);
    font-family: "Open Sans", sans-serif;
  }
  .canvas { position: relative; width: 1200px; height: 1200px; }
  .card {
    position: absolute; left: 180px;
    width: 840px; height: 480px;
    background: var(--paper);
    box-shadow: 0 10px 30px var(--card-shadow);
    overflow: hidden;
  }
  .card--front { top: 90px; }
  .card--back { top: 630px; }

  /* Front */
  .front__band {
    position: absolute; left: 0; top: 0; width: 100%; height: 240px;
    background: var(--brand-blue);
  }
  .front__side-strip {
    position: absolute; right: 0; top: 240px; width: 100px; height: 150px;
    background: var(--brand-blue);
  }
  .front__brand { position: absolute; left: 60px; top: 62px; color: var(--paper); }
  .brand-name { font-weight: 600; font-size: 42px; letter-spacing: 2px; line-height: 1; }
  .brand-tagline { margin-top: 10px; font-size: 15px; letter-spacing: 0.5px; font-weight: 400; }
  .front__person { position: absolute; left: 60px; top: 290px; color: var(--ink); }
  .person-name { font-size: 32px; font-weight: 400; }
  .person-role { margin-top: 6px; font-size: 15px; font-weight: 600; }

  .contact-panel {
    position: absolute; left: 480px; top: 216px; width: 260px; height: 264px;
    background: var(--paper);
    padding: 22px 0 0 22px;
    list-style: none;
  }
  .contact-item {
    display: flex; align-items: flex-start; gap: 16px;
    font-size: 14px; line-height: 19px; color: var(--ink);
    margin-bottom: 12px;
  }
  .contact-icon { width: 18px; height: 18px; flex: none; margin-top: 1px; fill: var(--brand-blue); }

  /* Back */
  .back__brand { position: absolute; left: 0; top: 150px; width: 100%; text-align: center; color: var(--brand-blue); }
  .back__brand .brand-name { font-size: 64px; letter-spacing: 3px; }
  .back__brand .brand-tagline { font-size: 20px; margin-top: 14px; }
  .back__web {
    position: absolute; left: 0; top: 340px; width: 100%;
    text-align: center; color: var(--brand-blue);
    font-size: 24px; font-weight: 600;
  }
</style>
</head>
<body>
<main class="canvas">
  <section class="card card--front" aria-label="Business card front">
    <div class="front__band"></div>
    <div class="front__side-strip"></div>
    <div class="front__brand">
      <div class="brand-name">BRIGHTWELL</div>
      <div class="brand-tagline">Framing Moments. Telling Stories.</div>
    </div>
    <div class="front__person">
      <div class="person-name">Marina Solano</div>
      <div class="person-role">Founder &amp; Media Director</div>
    </div>
    <ul class="contact-panel">
      <li class="contact-item">
        <svg class="contact-icon" viewBox="0 0 24 24"><path d="M6.6 10.8a15 15 0 0 0 6.6 6.6l2.2-2.2c.3-.3.7-.4 1-.2 1.1.4 2.300.6 3.6.6.6 0 1 .4 1 1V20c0 .6-.4 1-1 1A17 17 0 0 1 3 4c0-.6.4-1 1-1h3.5c.6 0 1 .4 1 1 0 1.3.2 2.5.6 3.6.1.3 0 .7-.2 1z"/></svg>
        <span>(555) 014-2290</span>
      </li>
      <li class="contact-item">
        <svg class="contact-icon" viewBox="0 0 24 24"><path d="M2 5h20v14H2zM4 7v.4l8 5 8-5V7l-8 5z"/></svg>
        <span>mar@brightwellmedia.com</span>
      </li>
      <li class="contact-item">
        <svg class="contact-icon" viewBox="0 0 24 24"><path d="M12 3 2 12h3v8h5v-5h4v5h5v-8h3z"/></svg>
        <span>240 Harbor Av 9th Floor<br>Bayview, FL 33000</span>
      </li>
      <li class="contact-item">
        <svg class="contact-icon" viewBox="0 0 24 24"><path d="M12 2a10 10 0 1 0 0 20 10 10 0 0 0 0-20zm6.9 6h-3a15 15 0 0 0-1.3-3.9A8 8 0 0 1 18.9 8zM12 4c.8 1.2 1.5 2.5 1.9 4h-3.8c.4-1.5 1.1-2.8 1.9-4zM4.3 14a8 8 0 0 1 0-4h3.4a16 16 0 0 0 0 4zm.8 2h3a15 15 0 0 0 1.3 3.9A8 8 0 0 1 5.1 16zm3-8h-3a8 8 0 0 1 4.3-3.9C8.8 5.3 8.4 6.6 8.1 8zM12 20c-.8-1.2-1.5-2.5-1.9-4h3.8c-.4 1.5-1.1 2.8-1.9 4zm2.3-6H9.7a14 14 0 0 1 0-4h4.6a14 14 0 0 1 0 4zm.3 5.9c.6-1.2 1-2.5 1.3-3.9h3a8 8 0 0 1-4.3 3.9zm1.7-5.9a16 16 0 0 0 0-4h3.4a8 8 0 0 1 0 4z"/></svg>
        <span>mar@brightwellmedia.com</span>
      </li>
      <li class="contact-item">
        <svg class="contact-icon" viewBox="0 0 24 24"><path d="M12 2a7 7 0 0 0-7 7c0 5 7 13 7 13s7-8 7-13a7 7 0 0 0-7-7zm0 9.5A2.5 2.5 0 1 1 12 6.5a2.5 2.5 0 0 1 0 5z"/></svg>
        <span>Bayview • Port Alden •<br>Cedar Falls • Lumen • Vela</span>
      </li>
    </ul>
  </section>

  <section class="card card--back" aria-label="Business card back">
    <div class="back__brand">
      <div class="brand-name">BRIGHTWELL</div>
      <div class="brand-tagline">Framing Moments. Telling Stories.</div>
    </div>
    <div class="back__web">www.brightwellmedia.com</div>
  </section>
</main>
</body>
</html>
```